Masonry and Landscaping Construction company business card

Looking for a business card design for a construction company named Ferrano Construction. It is an italian-american family business that specializes in custom stone work, patios, walkways, driveways, steps, outdoor kitchens, concrete, waterproofing, power wash, landscaping and more. Our colors are mostly red and white with some black. We're looking for a bold design. we also like to incorporate a picture of my family's hometown somewhere in it.
Target Market(s)
Luxury home owners
Industry/Entity Type
Construction
Contact Information for Business Card
Details includes should be bullet points mentioning the services provided. Custom Stone Work, Outdoor Kitchens, Fire Pits, Patios, Walkways, Steps, Concrete, Waterproofing, powerwash and landscaping
Requirements
Must have
- Would like a spot on the card for co-owners names, numbers and email to be listed also looking to add the QR code for an instagram page
Nice to have
- would like something bold, based around the colors red and white with black outlines or details

```html
<!DOCTYPE html>
<html lang="en">
<head>
<meta charset="utf-8">
<title>Ferrano Construction – Business Card</title>
<link href="https://fonts.googleapis.com/css2?family=Archivo:wght@500;700;800&display=swap" rel="stylesheet">
<style>
  :root{
    --page:#e9e9e9;
    --card-dark:#231f20;
    --red:#c8102e;
    --red-text:#e0202e;
    --green:#1fb24a;
    --white:#ffffff;
    --grey:#8a8a8a;
    --text-light:#f2f2f2;
  }
  *{margin:0;padding:0;box-sizing:border-box}
  html,body{width:1200px;height:900px;overflow:hidden;background:var(--page)}
  body{position:relative;font-family:"Archivo",Arial,sans-serif}
  .card{position:absolute;left:250px;width:700px;height:400px;border-radius:26px;overflow:hidden;box-shadow:0 8px 24px rgba(0,0,0,.18)}
  .card-front{top:35px}
  .card-back{top:465px;background:var(--card-dark)}

  .hometown-photo{position:absolute;inset:0;
    background:linear-gradient(180deg,#dfe3e6 0%,#c9cfd3 18%,#6f8a5c 36%,#4f6e3e 55%,#a58a6c 72%,#8b7a5e 88%,#4c6b34 100%)}
  .brand-mark{position:absolute;left:0;right:0;top:138px;display:flex;align-items:center;justify-content:center;gap:14px}
  .brand-mark .mark-square{width:34px;height:34px;background:var(--red)}
  .brand-mark .brand-name{font-weight:800;font-size:40px;color:var(--white);text-transform:uppercase;letter-spacing:1px}

  .back-bands{position:absolute;inset:0}
  .contact{position:absolute;left:40px;top:110px;color:var(--text-light)}
  .contact .person-name{font-weight:700;font-size:26px;color:var(--red-text);text-transform:uppercase;line-height:1}
  .contact .person-role{font-weight:500;font-size:15px;color:var(--green);margin-top:4px}
  .contact .phone{font-weight:700;font-size:28px;margin-top:14px}
  .contact .email{font-weight:500;font-size:15px;margin-top:6px}
  .services{position:absolute;left:460px;top:34px;list-style:none;color:var(--text-light);font-weight:500;font-size:13px;line-height:16px;text-transform:uppercase}
  .services li::before{content:"";display:inline-block;width:4px;height:4px;background:var(--red);border-radius:50%;margin:0 8px 3px 0;vertical-align:middle}
</style>
</head>
<body>

<section class="card card-front">
  <div class="hometown-photo" role="img" aria-label="Photograph of the family's Italian hometown: stone bell tower, old village houses and green hills under a cloudy sky"></div>
  <div class="brand-mark">
    <span class="mark-square"></span>
    <span class="brand-name">Ferrano Construction</span>
  </div>
</section>

<section class="card card-back">
  <svg class="back-bands" width="700" height="400" viewBox="0 0 700 400">
    <defs>
      <linearGradient id="machinery" x1="0" y1="0" x2="1" y2="1">
        <stop offset="0" stop-color="#d9d9d9"/>
        <stop offset="1" stop-color="#6d6d6d"/>
      </linearGradient>
    </defs>
    <polygon points="300,196 700,196 700,210 292,210" fill="var(--grey)"/>
    <polygon points="0,318 286,212 700,212 700,222 300,222 0,340" fill="var(--white)"/>
    <polygon points="520,222 700,222 700,292 600,340" fill="var(--red)"/>
    <polygon points="0,346 110,304 150,400 0,400" fill="var(--green)"/>
    <rect x="140" y="232" width="480" height="160" rx="10" fill="url(#machinery)" role="img" aria-label="Illustration of a skid-steer loader and a dump truck"/>
  </svg>

  <div class="contact">
    <p class="person-name">Marco Bellini</p>
    <p class="person-role">managing director</p>
    <p class="phone">555 0142 3386</p>
    <p class="email">info@ferranoconstr.com</p>
  </div>

  <ul class="services">
    <li>Custom Stone Work</li>
    <li>Outdoor Kitchens</li>
    <li>Fire Pits &amp; Patios</li>
    <li>Walkways &amp; Steps</li>
    <li>Concrete</li>
    <li>Waterproofing</li>
    <li>Powerwash</li>
    <li>Landscaping</li>
  </ul>
</section>

</body>
</html>
```